5 website banners (slides show)

We need 5 website sliding banners created for a website all about internet safety. The topics for each banner are:

Cyberbullying
Fraud
seniors
social networking

Sizes: 953 pixels x 281 pixels

I have stock images to use or feel free to use your own or one I can purchase from pixelvarro.example.

Industry/Entity Type

Internet

```html
<!DOCTYPE html>
<html lang="en">
<head>
<meta charset="utf-8">
<title>Safenetic – Online Safety and Security</title>
<link href="https://fonts.googleapis.com/css2?family=Ubuntu:wght@400;500;700&family=Alegreya:ital,wght@1,400&family=Arimo:wght@400&display=swap" rel="stylesheet">
<style>
  :root{
    --pink:#ec008c;
    --pink-dark:#c4006f;
    --pink-soft:#f06db8;
    --green:#7dc22e;
    --green-dark:#6aad22;
    --green-light:#8ccf39;
    --text-grey:#8a98a6;
    --white:#ffffff;
  }
  *{box-sizing:border-box;margin:0;padding:0}
  html,body{width:1200px;height:900px;overflow:hidden;background:var(--white)}
  body{position:relative;font-family:"Arimo",Arial,sans-serif}

  .topbar{position:absolute;left:128px;top:7px;width:950px;height:34px;background:var(--pink);border-radius:4px}
  .topbar__links{position:absolute;left:15px;top:9px;display:flex;gap:25px}
  .topbar__links a{color:var(--white);font-size:13px;text-decoration:none}
  .topbar__social{position:absolute;left:610px;top:5px;width:24px;height:24px;background:#3b5a9a;border-radius:3px}
  .topbar__search{position:absolute;left:639px;top:2px;width:280px;height:30px;background:linear-gradient(#ffffff,#eef7fa);font-size:12px;color:#c56ba4;padding:8px 12px}
  .topbar__button{position:absolute;left:919px;top:4px;width:26px;height:26px;background:var(--pink);border-radius:3px}

  .brand{position:absolute;left:145px;top:55px}
  .brand__mark{position:absolute;left:0;top:0;width:98px;height:108px;border-radius:50%;background:var(--pink-soft)}
  .brand__name{position:absolute;left:113px;top:14px;font-family:"Ubuntu",sans-serif;font-weight:500;font-size:54px;color:var(--pink);letter-spacing:-1.5px;white-space:nowrap;line-height:1}
  .brand__tagline{position:absolute;left:115px;top:70px;font-family:"Ubuntu",sans-serif;font-size:13px;color:var(--green-dark);white-space:nowrap}

  .report{position:absolute;left:722px;top:63px;width:356px;height:96px;background:linear-gradient(#8dd13a,#74b92a);border-radius:3px;text-decoration:none}
  .report__frame{position:absolute;left:7px;top:7px;right:7px;bottom:7px;border:1px dashed rgba(255,255,255,.8)}
  .report__title{position:absolute;left:17px;top:15px;font-family:"Ubuntu",sans-serif;font-weight:700;font-size:20px;color:var(--white);letter-spacing:-.3px}
  .report__click{position:absolute;left:185px;top:41px;font-family:"Ubuntu",sans-serif;font-size:13px;color:var(--white)}
  .report__call{position:absolute;left:14px;top:56px;font-family:"Ubuntu",sans-serif;font-weight:700;font-size:23px;letter-spacing:-.6px;color:var(--white);white-space:nowrap}
  .report__badge{position:absolute;left:268px;top:4px;width:72px;height:88px;background:linear-gradient(#b9c6d4,#6d86a4);border-radius:8px 8px 36px 36px}

  .mainnav{position:absolute;left:128px;top:177px;width:950px;height:67px;background:var(--green-light);border-radius:6px;overflow:hidden}
  .mainnav__bar{position:absolute;left:0;top:0;width:100%;height:56px;background:var(--green);display:flex}
  .mainnav__item{height:56px;padding:0 18px;line-height:54px;font-family:"Ubuntu",sans-serif;font-size:15px;color:var(--white);border-right:2px solid #9bd364;white-space:nowrap}
  .mainnav__item--active{background:linear-gradient(#8ed23f,#74bb29)}

  .slide{position:absolute;left:126px;top:252px;width:953px;height:281px;overflow:hidden;background:radial-gradient(circle at 70% 30%,#f04ba8,#d70a80 70%)}
  .slide__photo{position:absolute;left:0;top:0;width:953px;height:281px;background:linear-gradient(100deg,#c9cfd6,#8ea0b8 45%,#6d7f96);clip-path:polygon(0 0,494px 0,342px 281px,0 281px)}
  .slide__edge{position:absolute;left:0;top:0}
  .slide__tag{position:absolute;left:620px;top:21px;padding:2px 6px;background:#b30065;border-radius:6px;font-family:"Ubuntu",sans-serif;font-size:17px;color:var(--white)}
  .slide__headline{position:absolute;left:548px;top:76px;font-family:"Alegreya",serif;font-style:italic;font-weight:400;font-size:37px;line-height:60px;color:var(--white);text-align:center;width:230px}

  .sidebar{position:absolute;left:128px;top:546px;width:220px;height:380px;background:var(--green-light);border-radius:8px}
  .sidebar__frame{position:absolute;left:10px;top:10px;right:10px;bottom:0;border:1px dashed rgba(255,255,255,.85);border-radius:8px}
  .sidebar__title{position:absolute;left:21px;top:31px;font-family:"Ubuntu",sans-serif;font-weight:500;font-size:15px;color:var(--white)}
  .sidebar__list{position:absolute;left:26px;top:62px;list-style:none}
  .sidebar__list li{font-size:12px;color:var(--white);height:25px}

  .content{position:absolute;left:358px;top:546px;width:717px;height:360px;background:var(--white);box-shadow:3px 0 4px rgba(0,0,0,.15)}
  .content__title{position:absolute;left:20px;top:21px;font-family:"Ubuntu",sans-serif;font-weight:700;font-size:25px;color:var(--pink)}
  .content__edit{position:absolute;left:20px;top:57px;font-size:12px;color:#c86ab9}
  .content__edit::before{content:"";display:inline-block;width:4px;height:4px;border-radius:50%;background:#9aa7b2;margin:0 11px 2px 0}
  .content__text{position:absolute;left:20px;top:91px;width:678px;font-size:12px;line-height:17px;color:var(--text-grey)}
  .content__text p{margin-bottom:18px}

  .audience{position:absolute;top:286px;width:200px}
  .audience__title{font-family:"Ubuntu",sans-serif;font-weight:500;font-size:15px;color:var(--pink);height:21px}
  .audience__photo{width:200px;height:60px;background:linear-gradient(#a58d7c,#6f5a4d)}
</style>
</head>
<body>
  <header class="topbar">
    <nav class="topbar__links"><a href="#">Home</a><a href="#">FAQs</a><a href="#">Contact</a></nav>
    <div class="topbar__social" aria-label="Social page"></div>
    <div class="topbar__search">Search...</div>
    <div class="topbar__button">
      <svg width="26" height="26" viewBox="0 0 26 26"><circle cx="11.5" cy="11.5" r="6" fill="none" stroke="#fff" stroke-width="2.6"/><line x1="16" y1="16" x2="21" y2="21" stroke="#fff" stroke-width="3" stroke-linecap="round"/></svg>
    </div>
  </header>

  <div class="brand">
    <div class="brand__mark"></div>
    <div class="brand__name">SAFENETIC</div>
    <div class="brand__tagline">BERMUDA ONLINE SAFETY AND SECURITY</div>
  </div>

  <a class="report" href="#">
    <div class="report__frame"></div>
    <div class="report__title">REPORT A CYBERCRIME</div>
    <div class="report__click">CLICK HERE</div>
    <div class="report__call">or call 1-555-010-4477</div>
    <div class="report__badge"></div>
  </a>

  <nav class="mainnav">
    <div class="mainnav__bar">
      <span class="mainnav__item mainnav__item--active">HOME</span>
      <span class="mainnav__item">ABOUT</span>
      <span class="mainnav__item">FOR PARENTS</span>
      <span class="mainnav__item">FOR TEENS</span>
      <span class="mainnav__item">FOR TWEENS</span>
      <span class="mainnav__item">FOR KIDS</span>
      <span class="mainnav__item">FOR TEACHERS</span>
      <span class="mainnav__item">RESOURCES</span>
    </div>
  </nav>

  <section class="slide">
    <div class="slide__photo" role="img" aria-label="Photo of a teacher helping a boy at a computer in a classroom"></div>
    <svg class="slide__edge" width="953" height="281" viewBox="0 0 953 281">
      <polygon points="494,0 500,0 348,281 342,281" fill="#ffffff"/>
      <polygon points="500,0 507,0 355,281 348,281" fill="#a8005e"/>
    </svg>
    <div class="slide__tag">#Fraud</div>
    <div class="slide__headline">Save And Smart<br>Internet Use</div>
  </section>

  <aside class="sidebar">
    <div class="sidebar__frame"></div>
    <h3 class="sidebar__title">CHOOSE AN ISSUE</h3>
    <ul class="sidebar__list">
      <li>Cyberbullying</li><li>Sexting</li><li>Internet Safety</li><li>Fraud</li>
      <li>Mobile Devices</li><li>Gangs</li><li>Blogging</li><li>Predators</li>
      <li>Copywriting</li><li>Social Networking</li><li>Gaming</li><li>eMailing, Chat Rooms</li>
    </ul>
  </aside>

  <main class="content">
    <h1 class="content__title">WELCOME</h1>
    <div class="content__edit">Edit</div>
    <div class="content__text">
      <p>Welcome to Safenetic, Bermuda’s source of information on internet safety, brought to you by the Office of Digital Wellbeing. Our aim is to provide practical tips, resources and contact information to help parents, children and educators to use the Internet safely and be on guard against online predators and other inappropriate online content.</p>
      <p>By knowing the dangers and how to avoid them, you can take advantage of all the positive aspects of the Internet while avoiding most of its pitfalls.</p>
      <p>The Office of Digital Wellbeing partners with the Island Police Service, Northgate Software, Kiwi Clicks Studio and a number of other organizations locally and internationally to bring innovative and media rich educational tools to Bermuda</p>
    </div>
    <div class="audience" style="left:10px"><div class="audience__title">KIDS</div><div class="audience__photo" role="img" aria-label="Photo of a child using a computer"></div></div>
    <div class="audience" style="left:245px"><div class="audience__title">TWEENS</div><div class="audience__photo" role="img" aria-label="Photo of a tween girl online"></div></div>
    <div class="audience" style="left:480px"><div class="audience__title">TEENS</div><div class="audience__photo" role="img" aria-label="Photo of a group of teenagers"></div></div>
  </main>
</body>
</html>
```